Live Webcasting Host Wants Template/Theme to Jumpstare Ecommerce Site

Please,Please, Please READ ALL OF THE DESCRIPTION. Thank you.

I need a template for a look for my developer to work with in designing an ecommerce site where clients pay a monthly fee for streaming services and video on demand.

I'll need 2 pages designed:
1) public page
2) client log in landing page.

Please use a CMS (WP preferred) as this will allow is for further content to be added after delivery. Please include the pricing text in boxes in slides (pdf) to help fill out you design for the home page.

The attached slides are to give you a general layout of how I envision the pages. Yes I would like the Client page to be tabbed from the side like in the attached slide.

I've attached company logos for use along with the accompanying .psd and .ai files in the zip. Use the colors in logo in site design.

Thank you for your time.

Please, no designs. This is for a CMS for webpage design like WordPress or Joomla. Thanks. Added Friday, January 13, 2017

Target Market(s)

Churches, Organizations, Civic Organizations, Government Agencies (State, Local) -BUT don't let this deter your creativity. Decision makers/influencers will be video production and/or IT personnel.

Industry/Entity Type

It Company

Font styles to use
Sans Serif

Colors
f5f5f5
e8e8e8
333333
fece3e
cbcbcb
33a6d7
000000

Requirements
Must have
• Responsive Design
Nice to have
• One Page Design
Should not have
• SHOULD NOT HAVE White overall background but use white in other ways if you like.

```html
<!DOCTYPE html>
<html lang="en">
<head>
<meta charset="utf-8">
<title>Vireo Live Media – Pricing</title>
<link href="https://fonts.googleapis.com/css2?family=Open+Sans:wght@400;600;700;800&display=swap" rel="stylesheet">
<style>
  :root{
    --orange:#f89c22;
    --orange-dark:#c9781a;
    --orange-shade:#e48d1b;
    --blue:#33a6d7;
    --charcoal:#333333;
    --black:#000000;
    --panel-grey:#e8e8e8;
    --bg-top:#cbcbcb;
    --bg-bottom:#e8e8e8;
    --white:#ffffff;
    --text:#3a3a3a;
    --muted:#5a5a5a;
    --social:#a3a3a3;
  }
  *{margin:0;padding:0;box-sizing:border-box}
  html,body{width:1200px;height:695px;overflow:hidden}
  body{font-family:"Open Sans",Arial,sans-serif;color:var(--text);background:var(--bg-bottom);position:relative}

  .site-header{position:absolute;left:0;top:0;width:1200px;height:96px;background:var(--white)}
  .brand{position:absolute;left:74px;top:28px;display:flex;align-items:center;gap:8px;font-size:34px;font-weight:700;color:var(--charcoal);letter-spacing:-0.5px;line-height:1}
  .brand-dot{width:22px;height:22px;border-radius:50%;background:var(--orange)}
  .main-nav{position:absolute;top:38px;left:0;font-size:15px;font-weight:600;color:var(--charcoal)}
  .main-nav a{position:absolute;white-space:nowrap;color:inherit;text-decoration:none;letter-spacing:.2px}
  .login-btn{position:absolute;left:1040px;top:29px;width:85px;height:35px;background:var(--orange);color:var(--white);border-radius:2px;font-size:14px;font-weight:700;display:flex;align-items:center;justify-content:center;letter-spacing:.3px}

  .pricing{position:absolute;left:0;top:96px;width:1200px;height:544px;background:linear-gradient(var(--bg-top),var(--bg-bottom))}
  .plan{position:absolute;top:66px;width:332px;height:413px;background:var(--white);border:1px solid #f2f2f2}
  .plan::after{content:"";position:absolute;left:20px;right:20px;bottom:-12px;height:14px;border-radius:50%;background:rgba(0,0,0,.18);filter:blur(6px);z-index:-1}
  .plan-head{height:101px;background:var(--panel-grey);text-align:center;padding-top:20px;font-size:20px;font-weight:800;color:var(--black);letter-spacing:.3px}
  .plan-price{position:absolute;left:50%;top:60px;width:83px;height:83px;margin-left:-41.5px;border-radius:50%;border:3px solid var(--white);color:var(--white);font-size:22px;font-weight:700;display:flex;align-items:center;justify-content:center}
  .plan-small .plan-price{background:var(--orange)}
  .plan-medium .plan-price{background:var(--blue)}
  .plan-large .plan-price{background:var(--charcoal)}
  .plan-icon{position:absolute;left:28px;top:162px}
  .plan-hours{position:absolute;left:91px;top:163px;width:205px}
  .hours-num{font-size:28px;font-weight:700;line-height:30px;color:var(--charcoal)}
  .hours-label{font-size:17px;font-weight:700;line-height:20px;color:var(--charcoal)}
  .hours-note{font-size:15px;line-height:18.5px;color:var(--muted);margin-top:2px}
  .plan-storage{position:absolute;left:91px;top:270px;width:200px;font-size:15px;font-weight:700;line-height:18.5px;color:#454545}
  .buy-btn{position:absolute;left:93px;top:342px;width:165px;height:48px;background:var(--orange);border-radius:3px;border-bottom:4px solid var(--orange-dark);display:flex;color:var(--white);font-size:16px;font-weight:700}
  .buy-btn span{flex:1;display:flex;align-items:center;padding-left:17px}
  .buy-btn i{width:38px;background:var(--orange-shade);display:flex;align-items:center;justify-content:center;border-radius:0 3px 3px 0}

  .site-footer{position:absolute;left:0;top:640px;width:1200px;height:55px;background:var(--white);font-size:14px;color:#555}
  .legal{position:absolute;left:79px;top:15px;white-space:nowrap}
  .legal .sep{margin:0 8px}
  .social{position:absolute;left:1048px;top:14px;display:flex;gap:1px}
  .social span{width:24px;height:24px;background:var(--social)}
</style>
</head>
<body>
  <header class="site-header">
    <div class="brand"><span>Vireo</span><span class="brand-dot"></span></div>
    <nav class="main-nav">
      <a style="left:368px">FEATURES</a>
      <a style="left:471px">PRICING</a>
      <a style="left:564px">ABOUT US</a>
      <a style="left:669px">WEBCASTING 101</a>
      <a style="left:826px">CONTACT</a>
    </nav>
    <div class="login-btn">LOG IN</div>
  </header>

  <main class="pricing">
    <section class="plan plan-small" style="left:73px">
      <div class="plan-head">SMALL</div>
      <div class="plan-price">$49</div>
      <svg class="plan-icon" width="46" height="48" viewBox="0 0 46 48" fill="none" stroke="#333" stroke-width="2.5"><path d="M26 8H2v32h40V26"/><path d="M2 44h30M36 44h2"/><path d="M14 16v16l13-8z" fill="#333" stroke="none"/><circle cx="35" cy="10" r="8" fill="#fff"/><path d="M35 6v4h3"/></svg>
      <div class="plan-hours"><div class="hours-num">400</div><div class="hours-label">Viewer Hours</div><div class="hours-note">(50 Viewers watching 2 hrs- 4 times per month)</div></div>
      <div class="plan-storage">100 GB/month of video Storage</div>
      <div class="buy-btn"><span>Buy Package</span><i><svg width="20" height="14" viewBox="0 0 20 14"><path d="M1 13C3 7 7 5 13 5V1l6 5.5-6 5.5V8C8 8 4 9 1 13z" fill="#fff"/></svg></i></div>
    </section>

    <section class="plan plan-medium" style="left:434px">
      <div class="plan-head">MEDIUM</div>
      <div class="plan-price">$399</div>
      <svg class="plan-icon" width="46" height="48" viewBox="0 0 46 48" fill="none" stroke="#333" stroke-width="2.5"><path d="M26 8H2v32h40V26"/><path d="M2 44h30M36 44h2"/><path d="M14 16v16l13-8z" fill="#333" stroke="none"/><circle cx="35" cy="10" r="8" fill="#fff"/><path d="M35 6v4h3"/></svg>
      <div class="plan-hours"><div class="hours-num">4000</div><div class="hours-label">Viewer Hours</div><div class="hours-note">(500 Viewers watching 2 hrs- 4 times per month)</div></div>
      <div class="plan-storage">500 GB/month of video Storage</div>
      <div class="buy-btn"><span>Buy Package</span><i><svg width="20" height="14" viewBox="0 0 20 14"><path d="M1 13C3 7 7 5 13 5V1l6 5.5-6 5.5V8C8 8 4 9 1 13z" fill="#fff"/></svg></i></div>
    </section>

    <section class="plan plan-large" style="left:793px">
      <div class="plan-head">LARGE</div>
      <div class="plan-price">$999</div>
      <svg class="plan-icon" width="46" height="48" viewBox="0 0 46 48" fill="none" stroke="#333" stroke-width="2.5"><path d="M26 8H2v32h40V26"/><path d="M2 44h30M36 44h2"/><path d="M14 16v16l13-8z" fill="#333" stroke="none"/><circle cx="35" cy="10" r="8" fill="#fff"/><path d="M35 6v4h3"/></svg>
      <div class="plan-hours"><div class="hours-num">16000</div><div class="hours-label">Viewer Hours</div><div class="hours-note">(2000 Viewers watching 2 hrs- 4 times per month)</div></div>
      <div class="plan-storage">2000 GB/month of video Storage</div>
      <div class="buy-btn"><span>Buy Package</span><i><svg width="20" height="14" viewBox="0 0 20 14"><path d="M1 13C3 7 7 5 13 5V1l6 5.5-6 5.5V8C8 8 4 9 1 13z" fill="#fff"/></svg></i></div>
    </section>
  </main>

  <footer class="site-footer">
    <div class="legal">© 2017 Vireo Live Media. All rights reserved<span class="sep">|</span>Privacy Policy<span class="sep">|</span>Terms of Use</div>
    <div class="social" aria-label="Social links"><span></span><span></span><span></span></div>
  </footer>
</body>
</html>
```